I need a simple, classy and stylish business card. I would like it to have a black background with white writing. I would like you to use my logo you designed on the front with the word 'Imagery" used underneath it in the same font. On the back I was thinking of the website at the top 'tomverrick.com' Then my social media accounts, Can you use the instagram, Facebook and twitter logo then my handles?
Please let me know what you think.
Regards Tom
Must have
- Website: www.tomverrick.com
- Social media handles..
- Instagram: @Tom_Verrick_Imagery
- Facebook: Tom Verrick Imagery
- Twitter: @Tom_Verrick
- Email: info@tomverick.com
- Phone: 0437 518 293

```html
<!DOCTYPE html>
<html lang="en">
<head>
<meta charset="utf-8">
<title>Tom Verrick Imagery – Business Card</title>
<link rel="stylesheet" href="https://fonts.googleapis.com/css2?family=Open+Sans:wght@400;600;700&display=swap">
<style>
  :root {
    --stage: #2b2622;
    --card: #0a0a0a;
    --card-sheen: #1c1c1c;
    --ink: #ffffff;
    --ink-soft: #cfcfcf;
    --ink-muted: #9a9a9a;
  }
  * { box-sizing: border-box; margin: 0; padding: 0; }
  html, body {
    width: 1200px; height: 843px; overflow: hidden;
    background: var(--stage);
    font-family: "Open Sans", Arial, sans-serif;
    color: var(--ink);
  }
  .stage {
    width: 1200px; height: 843px;
    display: flex; align-items: center; justify-content: center; gap: 60px;
  }
  .card {
    position: relative;
    width: 525px; height: 300px;
    background: linear-gradient(160deg, var(--card-sheen) 0%, var(--card) 45%, var(--card) 100%);
    box-shadow: 0 12px 30px rgba(0,0,0,.45);
    overflow: hidden;
  }
  .brand {
    display: flex; align-items: center; gap: 12px;
  }
  .brand-dot {
    width: 34px; height: 34px; border: 2px solid var(--ink); border-radius: 50%;
  }
  .brand-name {
    font-weight: 400; font-size: 26px; line-height: 1.05; color: var(--ink);
  }
  /* Front */
  .card--front .brand {
    position: absolute; left: 50%; top: 110px; transform: translateX(-50%);
  }
  .card--front .web {
    position: absolute; left: 0; right: 0; top: 205px; text-align: center;
    font-size: 13px; letter-spacing: 6px; color: var(--ink-soft);
  }
  /* Back */
  .card--back .brand {
    position: absolute; right: 34px; top: 52px;
  }
  .card--back .brand-name { font-size: 22px; }
  .contacts {
    position: absolute; left: 34px; top: 112px;
    list-style: none; font-size: 14px; line-height: 21px; color: var(--ink-soft);
  }
  .contacts li { display: flex; align-items: center; gap: 10px; }
  .contacts svg { width: 12px; height: 12px; flex: none; }
  .person {
    position: absolute; right: 34px; bottom: 40px; text-align: right;
  }
  .person-name { font-size: 19px; font-weight: 700; color: var(--ink-soft); letter-spacing: .5px; }
  .person-role { font-size: 14px; color: var(--ink-muted); }
</style>
</head>
<body>
<main class="stage">
  <section class="card card--front" aria-label="Card front">
    <div class="brand">
      <span class="brand-dot"></span>
      <span class="brand-name">Tom Verrick<br>Imagery</span>
    </div>
    <p class="web">www.tomverrick.com</p>
  </section>

  <section class="card card--back" aria-label="Card back">
    <ul class="contacts">
      <li>
        <svg viewBox="0 0 12 12" aria-hidden="true"><path d="M3 1l2 2.5-1.2 1.2c.7 1.5 1.8 2.6 3.3 3.3L8.3 6.8 11 9l-1 2C5 11 1 7 1 2z" fill="#fff"/></svg>
        0437 518 293
      </li>
      <li>
        <svg viewBox="0 0 12 12" aria-hidden="true"><circle cx="6" cy="6" r="5" fill="none" stroke="#fff" stroke-width="1.3"/><path d="M1 6h10M6 1c-2.5 3-2.5 7 0 10M6 1c2.5 3 2.5 7 0 10" fill="none" stroke="#fff" stroke-width="1"/></svg>
        www.tomverrick.com
      </li>
      <li>
        <svg viewBox="0 0 12 12" aria-hidden="true"><rect x="1" y="1" width="10" height="10" fill="#fff"/></svg>
        @Tom_Verrick_Imagery
      </li>
      <li>
        <svg viewBox="0 0 12 12" aria-hidden="true"><rect x="1" y="1" width="10" height="10" fill="#fff"/></svg>
        @TomVerrickImagery
      </li>
      <li>
        <svg viewBox="0 0 12 12" aria-hidden="true"><circle cx="6" cy="6" r="5" fill="#fff"/></svg>
        Tom_Verrick
      </li>
    </ul>

    <div class="brand">
      <span class="brand-dot"></span>
      <span class="brand-name">Tom Verrick<br>Imagery</span>
    </div>

    <div class="person">
      <p class="person-name">JOHN SMITH</p>
      <p class="person-role">CEO/Founder</p>
    </div>
  </section>
</main>
</body>
</html>
```